A Glimpse of Coral Plains food and wine tours

we need a DL size flyer, front and back.
A Glimpse of Coral Plains
we offer food and wine tours in South Australia and its 5 wine regions, expert food and wine guide,
we would like to see fresh, classy, simple and eye catching design
we want to clearly show people the tour options we offer clients,
good to be used by differing markets
showcasing south australian tourism

target market is in tourism industry, domestic and international
we want to invite all to see our flyer including luxury market
rich red in logo with black and white design , colour same as business card, cherry red , dark red

Reason: Like what they have produced but been to busy to offer suggested changes, so need to extend a little longer cheers lucy ellen

Tourism

Must have
• our complany logo
simple points of the tours we offer:
we would like the logo on the front
with key dot points and photo below & clear contact detials
key dot points and tour options listed on the back
Key words & ideas : unique, luxury, bespoke, extensive local knowledge of food and wine producers, based in Adelaide pickk up from all regions, customize, gourmet , relationships with premium wine producers, insiders knowledge , introduce you to the locals, accredited

A Glimpse of Coral Plains offers bespoke fine food and wine touring experiences to our stunning wine regions. We have 23 years experience ensuring our guests have enjoy premium touring!

• we offer tours of all the main regions of South Australia, Barossa Valley, McLaren Vale, Adelaide Hills & Clare Valley and surrounds. We offer private touring and boutique share tours.
• Our passionate guides have an unbeatable knowledge for visitors to draw on. Visitors will meet the makers behind the State’s best food and wine, sample their products, and experience the hospitality of friendly locals.
• A Glimpse of Coral Plains offers tours ranging from 4 daily departure share tours from 2-5 pax, to extended tailor-made tours, catering for serious wine buffs as well as those who want fun, hands-on food and wine experiences.
•boutique share tours Finest of Kellerby, Dunmore ridge food and wine tour, Wrenhaven Fine food wine and wildlife, Sample of Ormond Heights
• Lively Locals Brenton walking tours: Upper Quarter Tavern Life, Riverside Crafts and Customs, Timeless Brenton -Customs and Legacy , Bazaar Rambles
• pick and drop off location, just ask and we can assist with city, seaside or country pick up locations
• We tailor make tours to suit your needs
• More information: www.glimpsecp.example.au

```html
<!DOCTYPE html>
<html lang="en">
<head>
<meta charset="utf-8">
<title>A Glimpse of Coral Plains – Tours</title>
<link href="https://fonts.googleapis.com/css2?family=Arimo:wght@400;700&display=swap" rel="stylesheet">
<style>
  :root {
    --cherry: #84181c;
    --ink: #1e1e1e;
    --paper: #ffffff;
  }
  * { margin: 0; padding: 0; box-sizing: border-box; }
  html, body { width: 1200px; height: 900px; overflow: hidden; background: var(--paper); }
  body { font-family: "Arimo", Arial, sans-serif; position: relative; color: var(--paper); }

  .info-panel { position: absolute; left: 2px; top: 143px; width: 605px; height: 483px; background: var(--cherry); }
  .intro { position: absolute; left: 31px; top: 28px; width: 505px; font-size: 14px; font-weight: 700; line-height: 27px; }
  .point { position: absolute; left: 72px; width: 492px; font-size: 14px; line-height: 26px; }
  .point-icon { position: absolute; left: 30px; }

  .contact-band { position: absolute; left: 0; top: 626px; width: 607px; height: 90px; background: var(--ink); padding: 2px 0 0 75px; }
  .contact-band p { font-size: 14px; font-weight: 700; line-height: 27px; letter-spacing: 0.2px; }

  .tours-title { position: absolute; left: 648px; top: 168px; color: var(--cherry); font-size: 17px; font-weight: 700; line-height: 34px; z-index: 2; }

  .region-map { position: absolute; left: 620px; top: 195px; width: 580px; height: 460px; }

  .map-label { position: absolute; font-size: 14px; font-weight: 700; line-height: 27px; color: var(--paper); white-space: nowrap; }
  .map-label.dark { color: var(--cherry); }
  .num { position: absolute; width: 26px; height: 26px; border-radius: 50%; background: var(--paper); color: var(--cherry); font-size: 11px; font-weight: 700; text-align: center; line-height: 26px; letter-spacing: 1px; }
  .divider { position: absolute; left: 879px; top: 464px; width: 268px; height: 1px; background: var(--paper); }
  .glass { position: absolute; }
</style>
</head>
<body>

<section class="info-panel">
  <p class="intro">A Glimpse of Coral Plains offers bespoke fine food &amp; wine touring experiences to our stunning wine regions. We have 23 years experience ensuring our guests have enjoy premium touring!</p>

  <svg class="point-icon" style="top:140px" width="28" height="60" viewBox="0 0 28 60" aria-hidden="true">
    <path d="M4 2h20c1 12 0 22-10 25C4 24 3 14 4 2z" fill="none" stroke="#fff" stroke-width="2.5"/>
    <path d="M5 12h18c-1 8-4 13-9 14-5-1-8-6-9-14z" fill="#fff"/>
    <path d="M14 27v27M5 56h18" stroke="#fff" stroke-width="2.5"/>
  </svg>
  <p class="point" style="top:132px">We offer tours of all the main regions of South Australia, Barossa Valley, McLaren Vale, Adelaide Hills &amp; Clare Valley and surrounds.<br>We offer private touring and boutique share tours.</p>

  <svg class="point-icon" style="top:235px" width="28" height="60" viewBox="0 0 28 60" aria-hidden="true">
    <path d="M4 2h20c1 12 0 22-10 25C4 24 3 14 4 2z" fill="none" stroke="#fff" stroke-width="2.5"/>
    <path d="M5 12h18c-1 8-4 13-9 14-5-1-8-6-9-14z" fill="#fff"/>
    <path d="M14 27v27M5 56h18" stroke="#fff" stroke-width="2.5"/>
  </svg>
  <p class="point" style="top:228px">Our passionate guides have an unbeatable knowledge for visitors to draw on. Visitors will meet the makers behind the State’s best food &amp; wine, sample their products and experience the hospitality of friendly locals.</p>

  <svg class="point-icon" style="top:333px" width="30" height="90" viewBox="0 0 30 90" aria-hidden="true">
    <path d="M11 2h8v24c0 6 10 10 10 20v42H1V46c0-10 10-14 10-20z" fill="#fff"/>
    <rect x="6" y="52" width="18" height="24" fill="#84181c"/>
  </svg>
  <p class="point" style="top:326px">A Glimpse of Coral Plains offers tours ranging from 4 daily departure share tours from 2-5 pax, to extended tailor-made tours, catering for serious wine buffets as well as those who want fun, hands-on food and wine experiences.</p>
</section>

<footer class="contact-band">
  <p>A Glimpse of Coral Plains, GPO BOX 418 Brenton, SA 5099</p>
  <p>Telephone: +61 8 8000 4172</p>
  <p>Website: www.glimpsecp.example.au</p>
</footer>

<svg class="region-map" viewBox="620 195 580 460" role="img" aria-label="Map of Australia showing the tour regions around South Australia">
  <path fill="#84181c" d="M632 300C632 262 655 250 690 250L980 250C1010 250 1020 205 1050 205C1100 205 1192 250 1192 330L1192 560C1192 610 1150 640 1110 640L1040 640C1010 640 1000 600 970 600L680 600C650 600 632 580 632 555Z"/>
</svg>

<h2 class="tours-title">You can find our tours<br>here...</h2>

<svg style="position:absolute;left:662px;top:396px" width="46" height="26" viewBox="0 0 46 26" aria-hidden="true">
  <path d="M6 18c0-10 7-16 17-16s17 6 17 16z" fill="#fff"/>
  <rect x="1" y="18" width="44" height="5" rx="2.5" fill="#fff"/>
</svg>
<p class="map-label" style="left:718px;top:384px">We tailor make tours<br>to suit your needs.</p>

<svg style="position:absolute;left:664px;top:450px" width="42" height="40" viewBox="0 0 42 40" aria-hidden="true">
  <rect x="15" y="1" width="12" height="5" fill="#fff"/>
  <path d="M8 8h26l5 12v14H3V20z" fill="#fff"/>
  <rect x="10" y="11" width="22" height="8" fill="#84181c"/>
  <circle cx="10" cy="27" r="3" fill="#84181c"/><circle cx="32" cy="27" r="3" fill="#84181c"/>
  <rect x="5" y="33" width="7" height="6" fill="#fff"/><rect x="30" y="33" width="7" height="6" fill="#fff"/>
</svg>
<p class="map-label" style="left:719px;top:444px">Pick &amp; Drop-Off<br>location, just ask.</p>

<span class="num" style="left:847px;top:332px">02</span>
<p class="map-label" style="left:879px;top:330px">Lively Locals Brenton Walking Tours<br>+ Upper Quarter Tavern Life<br>+ Riverside Crafts &amp; Customs<br>+ Timeless Brenton - Customs &amp; Legacy<br>+ Bazaar Rambles</p>
<div class="divider"></div>

<span class="num" style="left:847px;top:481px">01</span>
<p class="map-label" style="left:881px;top:466px">Sample of<br>Ormond Heights</p>

<svg class="glass" style="left:994px;top:486px" width="50" height="70" viewBox="0 0 50 70" aria-hidden="true">
  <g fill="none" stroke="#fff" stroke-width="2.5">
    <path d="M3 14h18c2 14-2 22-9 22S1 28 3 14z"/><path d="M12 36v30M5 67h14"/>
    <path d="M26 2h18c2 14-2 22-9 22S24 16 26 2z"/><path d="M35 24v38M28 63h14"/>
  </g>
</svg>
<span class="num" style="left:1040px;top:506px">03</span>
<p class="map-label" style="left:1070px;top:505px">Finest of Kellerby</p>

<svg class="glass" style="left:1005px;top:550px" width="26" height="60" viewBox="0 0 26 60" aria-hidden="true">
  <g fill="none" stroke="#fff" stroke-width="2.5">
    <path d="M4 2h18c2 14-2 22-9 22S2 16 4 2z"/><path d="M13 24v32M6 57h14"/>
  </g>
</svg>
<span class="num" style="left:1039px;top:545px">04</span>
<p class="map-label" style="left:1033px;top:570px">Dunmore Ridge<br>Food &amp; Wine</p>

<svg class="glass" style="left:945px;top:612px" width="26" height="58" viewBox="0 0 26 58" aria-hidden="true">
  <path d="M3 2h20c2 14-2 22-10 22S1 16 3 2z" fill="#84181c"/>
  <path d="M13 24v30M5 55h16" stroke="#84181c" stroke-width="3"/>
</svg>
<span class="num" style="left:968px;top:617px;background:var(--cherry);color:#fff">05</span>
<p class="map-label dark" style="left:876px;top:614px">Wrenhaven<br>Fine Food<br>Wine &amp; Wildlife</p>

</body>
</html>
```